Book cover needed for self help business book

Book cover needed and I will provide back cover blurb and barcode to the winning designer. Book may be too small for spine, but I will give you the page number details to confirm. Book information below:

Title: Nine Seasons of Resale
Subtitle: Proven Grindstone Methods for the Modern Marketplace
Author: DeMarco Pellet

Design should be clean, modern, and bold—something that appeals to everyday entrepreneurs and resellers. The cover should reflect grit, real-world hustle, and long-term wisdom without looking overly corporate or flashy. I am open to your creative ideas.

I am open to modern designs, but also designs of rugged old covers that simulate a book that may have aged over the years.

I prefer not to have pictures or silhouettes of people

Requirements
Nice to have
• I am open to modern designs, but also designs of rugged old covers that simulate a book that may have aged over the years.
Should not have
• Pictures or silhouettes of people

```html
<!DOCTYPE html>
<html lang="en">
<head>
<meta charset="utf-8">
<title>Nine Seasons of Resale — Front Cover</title>
<link rel="stylesheet" href="https://fonts.googleapis.com/css2?family=Oswald:wght@700&family=Montserrat:wght@700&display=swap">
<style>
  :root {
    --backdrop: #cdcdd0;
    --parchment-light: #ecd7a6;
    --parchment-mid: #d9b57a;
    --parchment-edge: #b98a4e;
    --title-top: #7b4535;
    --title-bottom: #561a0e;
    --rule-ink: #1e1a14;
    --subtitle-ink: #14110c;
    --band: #4a0b07;
    --band-edge: #360604;
    --author-ink: #d6b57a;
  }
  * { box-sizing: border-box; margin: 0; padding: 0; }
  html, body {
    width: 1200px;
    height: 800px;
    overflow: hidden;
    background: var(--backdrop);
  }
  .canvas {
    position: relative;
    width: 1200px;
    height: 800px;
    display: flex;
    align-items: center;
    justify-content: center;
  }
  .cover {
    position: relative;
    width: 494px;
    height: 740px;
    overflow: hidden;
    display: flex;
    flex-direction: column;
    align-items: center;
  }
  .cover__texture {
    position: absolute;
    inset: 0;
    background:
      radial-gradient(ellipse at 50% 45%, var(--parchment-light) 0%, var(--parchment-mid) 55%, var(--parchment-edge) 100%);
  }
  .title {
    position: relative;
    display: flex;
    flex-direction: column;
    align-items: center;
    margin-top: 34px;
    font-family: 'Oswald', 'Arial Narrow', sans-serif;
    font-weight: 700;
    text-transform: uppercase;
  }
  .title__word {
    display: block;
    line-height: 0.82;
    background: linear-gradient(180deg, var(--title-top), var(--title-bottom));
    -webkit-background-clip: text;
    background-clip: text;
    color: transparent;
  }
  .title__word--lead { font-size: 250px; letter-spacing: -2px; }
  .title__word--second { font-size: 128px; margin-top: 22px; }
  .title__word--last { font-size: 164px; margin-top: 8px; }
  .title__joiner {
    display: flex;
    align-items: center;
    gap: 12px;
    width: 426px;
    margin-top: 16px;
  }
  .title__rule {
    flex: 1;
    height: 2px;
    background: var(--rule-ink);
  }
  .title__small {
    font-size: 36px;
    line-height: 1;
    color: var(--rule-ink);
  }
  .subtitle {
    position: relative;
    margin-top: 30px;
    font-family: 'Montserrat', Arial, sans-serif;
    font-weight: 700;
    font-size: 14px;
    line-height: 1.5;
    text-align: center;
    text-transform: uppercase;
    color: var(--subtitle-ink);
  }
  .author-band {
    position: absolute;
    left: 0;
    right: 0;
    bottom: 0;
    height: 46px;
    background: linear-gradient(180deg, var(--band), var(--band-edge));
    display: flex;
    align-items: center;
    justify-content: center;
  }
  .author-band__name {
    font-family: 'Montserrat', Arial, sans-serif;
    font-weight: 700;
    font-size: 22px;
    letter-spacing: 7px;
    text-transform: uppercase;
    color: var(--author-ink);
  }
</style>
</head>
<body>
  <main class="canvas">
    <article class="cover">
      <div class="cover__texture" role="img" aria-label="Aged, weathered parchment texture in warm tan tones"></div>
      <h1 class="title">
        <span class="title__word title__word--lead">Nine</span>
        <span class="title__word title__word--second">Seasons</span>
        <span class="title__joiner">
          <span class="title__rule"></span>
          <span class="title__small">of</span>
          <span class="title__rule"></span>
        </span>
        <span class="title__word title__word--last">Resale</span>
      </h1>
      <p class="subtitle">Proven Grindstone Methods<br>for the Modern Marketplace</p>
      <footer class="author-band">
        <span class="author-band__name">DeMarco Pellet</span>
      </footer>
    </article>
  </main>
</body>
</html>
```